Service Proposal brochure

I have a list of services, references and details I can provide to create the service proposal from.

Target Market(s)

Project Managers in the Construction/Electrical Field Industry

Industry/Entity Type

Construction/Electrical Industry

Font styles to use
Serif

Colors
0054AA
0677BA
7BADD7
CADEEF
E8F1F8
FFF300
FFF600
FEFA6F
FFFEC7
FFFEE8

Requirements
Must have
• High vocabulary
Nice to have
• Creativity in the details of service work and layout of the brochure
Should not have
• So much wording that it becomes boring for the consumer

```html
<!DOCTYPE html>
<html lang="en">
<head>
<meta charset="utf-8">
<title>Construction / Electrical Industry – Service Flyer</title>
<link rel="stylesheet" href="https://fonts.googleapis.com/css2?family=Montserrat:wght@600;800&family=Open+Sans:wght@400;600&display=swap">
<style>
  :root{
    --blue-deep:#0054AA;
    --blue:#0677BA;
    --blue-mid:#7BADD7;
    --blue-pale:#CADEEF;
    --blue-mist:#E8F1F8;
    --ink:#1d3550;
    --white:#ffffff;
  }
  *{box-sizing:border-box;margin:0;padding:0}
  html,body{width:800px;height:1200px;overflow:hidden}
  body{background:var(--blue-mist);font-family:"Open Sans",Arial,sans-serif;color:var(--ink)}
  .flyer{position:relative;width:800px;height:1200px;overflow:hidden;
    background:linear-gradient(160deg,#f4f8fc 0%,var(--blue-mist) 45%,#dbe8f4 100%)}
  .hero{position:absolute;left:0;top:0;width:800px;height:460px}
  .headline{position:absolute;left:62px;top:468px;font-family:"Montserrat",Arial,sans-serif;font-weight:800;
    font-size:38px;line-height:1.12;letter-spacing:.5px;text-transform:uppercase}
  .headline .lead{color:var(--blue)}
  .headline .tail{color:var(--blue-deep)}
  .services-tag{position:absolute;left:62px;top:566px;padding:7px 26px 7px 20px;background:var(--blue);
    color:var(--white);font-family:"Montserrat",Arial,sans-serif;font-weight:600;font-size:19px;letter-spacing:1px;
    border-radius:0 22px 22px 0}
  .services{position:absolute;left:50px;top:640px;width:700px;display:grid;
    grid-template-columns:repeat(4,1fr);row-gap:26px;column-gap:10px}
  .service{display:flex;flex-direction:column;align-items:center;text-align:center}
  .service-icon{width:54px;height:54px;border:2px solid var(--blue);border-radius:50%;
    display:flex;align-items:center;justify-content:center;background:var(--white);margin-bottom:8px}
  .service-icon svg{width:26px;height:26px;stroke:var(--blue);fill:none;stroke-width:2;stroke-linecap:round;stroke-linejoin:round}
  .service-label{font-size:12.5px;line-height:1.3;color:var(--ink);max-width:140px}
  .contact-band{position:absolute;left:0;bottom:0;width:800px;height:110px}
  .contact{position:absolute;left:0;bottom:0;width:800px;height:84px;display:flex;align-items:center;
    justify-content:space-between;padding:0 56px;color:var(--white)}
  .phone{display:flex;align-items:center;gap:12px;font-family:"Montserrat",Arial,sans-serif;font-weight:800;font-size:28px;letter-spacing:.5px;white-space:nowrap}
  .phone svg{width:28px;height:28px;fill:var(--white)}
  .online{display:flex;gap:34px;font-size:13px;white-space:nowrap}
</style>
</head>
<body>
<main class="flyer">
  <svg class="hero" viewBox="0 0 800 460">
    <defs>
      <linearGradient id="plantTone" x1="0" y1="0" x2="1" y2="1">
        <stop offset="0" stop-color="#9fb3c4"/>
        <stop offset=".45" stop-color="#d9e2ea"/>
        <stop offset="1" stop-color="#7d93a8"/>
      </linearGradient>
      <clipPath id="heroShape">
        <path d="M0 0 H800 V300 C700 390 560 420 420 410 C260 400 120 360 40 290 C15 270 0 250 0 235 Z"/>
      </clipPath>
    </defs>
    <g clip-path="url(#heroShape)">
      <rect x="0" y="0" width="800" height="460" fill="url(#plantTone)" role="img" aria-label="Photo of an industrial plant interior with machinery, pipes and steel structures"/>
    </g>
    <path d="M0 0 H170 C110 30 70 80 55 140 C30 130 12 120 0 112 Z" fill="var(--blue-pale)" opacity=".85"/>
    <path d="M0 240 C60 330 180 390 330 412 C200 405 90 370 0 310 Z" fill="var(--blue)"/>
    <path d="M60 320 C170 400 350 440 520 430 C400 448 240 432 120 385 C90 370 70 350 60 320 Z" fill="var(--blue-mid)"/>
    <path d="M800 250 V330 C720 400 610 430 500 432 C620 410 720 360 800 250 Z" fill="var(--blue-deep)"/>
    <path d="M560 0 H800 V90 C740 40 660 10 560 0 Z" fill="var(--blue)"/>
    <path d="M650 0 H800 V45 C760 20 710 5 650 0 Z" fill="var(--blue-deep)"/>
  </svg>

  <h1 class="headline"><span class="lead">Construction/ Electrical</span><br><span class="tail">Industry</span></h1>
  <div class="services-tag">OUR BEST SERVICE'S</div>

  <section class="services">
    <div class="service"><span class="service-icon"><svg viewBox="0 0 24 24"><circle cx="11" cy="11" r="6"/><path d="M16 16l5 5"/></svg></span><p class="service-label">Site survey and<br>load planning</p></div>
    <div class="service"><span class="service-icon"><svg viewBox="0 0 24 24"><rect x="5" y="3" width="14" height="18" rx="1"/><path d="M9 8h6M9 12h6M9 16h3"/></svg></span><p class="service-label">Panel and switchgear<br>install</p></div>
    <div class="service"><span class="service-icon"><svg viewBox="0 0 24 24"><path d="M3 8h8a4 4 0 0 1 4 4v0a4 4 0 0 0 4 4h2"/><path d="M3 14h5"/></svg></span><p class="service-label">Conduit and cable<br>routing</p></div>
    <div class="service"><span class="service-icon"><svg viewBox="0 0 24 24"><path d="M9 18h6M10 21h4"/><path d="M12 3a6 6 0 0 0-3.5 10.9V16h7v-2.1A6 6 0 0 0 12 3z"/></svg></span><p class="service-label">Lighting design<br>and fitting</p></div>
    <div class="service"><span class="service-icon"><svg viewBox="0 0 24 24"><path d="M13 2L5 14h6l-1 8 8-12h-6z"/></svg></span><p class="service-label">Generator and<br>backup power</p></div>
    <div class="service"><span class="service-icon"><svg viewBox="0 0 24 24"><path d="M12 3l8 3v6c0 5-3.5 8-8 9-4.5-1-8-4-8-9V6z"/><path d="M8.5 12l2.5 2.5 4.5-5"/></svg></span><p class="service-label">Safety testing<br>and inspection</p></div>
    <div class="service"><span class="service-icon"><svg viewBox="0 0 24 24"><path d="M12 3v10M6 13h12M8 17h8M10.5 21h3"/></svg></span><p class="service-label">Grounding and<br>bonding works</p></div>
    <div class="service"><span class="service-icon"><svg viewBox="0 0 24 24"><path d="M6 17V11a6 6 0 0 1 12 0v6"/><path d="M4 17h16M10 20h4"/></svg></span><p class="service-label">Fire alarm<br>system wiring</p></div>
    <div class="service"><span class="service-icon"><svg viewBox="0 0 24 24"><circle cx="12" cy="12" r="4"/><path d="M12 2v3M12 19v3M2 12h3M19 12h3M5 5l2 2M17 17l2 2M5 19l2-2M17 7l2-2"/></svg></span><p class="service-label">Solar array<br>integration</p></div>
    <div class="service"><span class="service-icon"><svg viewBox="0 0 24 24"><circle cx="12" cy="12" r="3"/><circle cx="12" cy="12" r="8"/><path d="M12 4v3M12 17v3M4 12h3M17 12h3"/></svg></span><p class="service-label">Motor control<br>centers</p></div>
    <div class="service"><span class="service-icon"><svg viewBox="0 0 24 24"><rect x="4" y="5" width="16" height="15" rx="1"/><path d="M4 10h16M8 3v4M16 3v4"/></svg></span><p class="service-label">Preventive<br>maintenance plans</p></div>
    <div class="service"><span class="service-icon"><svg viewBox="0 0 24 24"><path d="M12 3L2 20h20z"/><path d="M12 9v5M12 17v.5"/></svg></span><p class="service-label">Emergency<br>fault repair</p></div>
    <div class="service"><span class="service-icon"><svg viewBox="0 0 24 24"><path d="M6 3h9l4 4v14H6z"/><path d="M9 13l2 2 4-4"/></svg></span><p class="service-label">Permit and code<br>compliance</p></div>
    <div class="service"><span class="service-icon"><svg viewBox="0 0 24 24"><circle cx="12" cy="12" r="9"/><path d="M12 7v5l3 2"/></svg></span><p class="service-label">Project scheduling<br>support</p></div>
    <div class="service"><span class="service-icon"><svg viewBox="0 0 24 24"><path d="M5 12l4 4L19 6"/></svg></span><p class="service-label">Commissioning<br>and handover</p></div>
    <div class="service"><span class="service-icon"><svg viewBox="0 0 24 24"><path d="M4 20V10M10 20V5M16 20v-7M22 20H2"/></svg></span><p class="service-label">Energy audit<br>reports</p></div>
  </section>

  <svg class="contact-band" viewBox="0 0 800 110" aria-hidden="true">
    <path d="M0 30 C200 10 600 10 800 30 V110 H0 Z" fill="var(--blue-mid)"/>
    <path d="M0 34 C200 20 600 20 800 34 V110 H0 Z" fill="var(--blue)"/>
  </svg>
  <footer class="contact">
    <div class="phone"><svg viewBox="0 0 24 24" aria-hidden="true"><path d="M6.6 10.8a15 15 0 0 0 6.6 6.6l2.2-2.2a1 1 0 0 1 1-.25 11.4 11.4 0 0 0 3.6.57 1 1 0 0 1 1 1V20a1 1 0 0 1-1 1A17 17 0 0 1 3 4a1 1 0 0 1 1-1h3.5a1 1 0 0 1 1 1c0 1.25.2 2.45.57 3.57a1 1 0 0 1-.25 1z"/></svg>(555) 014-2288</div>
    <div class="online"><span>info@voltarcbuild.com</span><span>www.voltarcbuild.com</span></div>
  </footer>
</main>
</body>
</html>
```